This is for a poster that will be hanging in the window of a Men's Suit Store in the mall:
Size 4 feet wide by 6 feet high
Main point is: A sale on "Suits" or "Men's Suits" at 40%-60% off ( the 40%-60% off should be the focal point)
Some words that can be used are "Sale" or "Clearance Sale"
Some key words that can be used to make it urgent are "limited time offer" or something similar.
You can get creative, the point is for the customer to want to come into the store and buy a suit right away.
You may use a graphic (picture of a man in a suit). It is not necessary but if it looks good you can use it. (If you do use a picture, it should be of a modern fit or slim fit suit)
Sorry, the initial brief somehow got deleted from the project. Please see the updated brief.
Thanks
Reason: Project was closed for some reason, extended to give enough time to complete
Target Market(s)
Mostly Men ages 35-55
Industry/Entity Type
Store
Colors
Designer to choose colors to be used in the design.

```html
<!DOCTYPE html>
<html lang="en">
<head>
<meta charset="UTF-8">
<title>Men's Suit Sale Poster</title>
<link rel="stylesheet" href="https://fonts.googleapis.com/css2?family=Arvo:wght@700&family=Josefin+Sans:wght@300&family=Questrial&display=swap">
<style>
  :root {
    --frame: #2b2b2e;
    --frame-edge: #3a3a3e;
    --navy: #2c3b7e;
    --sky-top: #c3c9dc;
    --sky-mid: #e3e7f0;
    --sky-bottom: #ffffff;
    --ink: #1c1c22;
    --photo-top: #c4cadb;
    --photo-suit: #2f3f7c;
    --photo-trouser: #eceef3;
    --photo-stool: #3b2a22;
  }
  * { margin: 0; padding: 0; box-sizing: border-box; }
  html, body { width: 807px; height: 1200px; overflow: hidden; }
  body { background: var(--frame); position: relative; }
  .frame {
    position: absolute;
    inset: 0;
    background: linear-gradient(90deg, var(--frame) 0%, var(--frame-edge) 50%, var(--frame) 100%);
  }
  .poster {
    position: absolute;
    left: 59px;
    top: 81px;
    width: 689px;
    height: 1027px;
    background: linear-gradient(180deg, var(--sky-top) 0%, var(--sky-mid) 45%, var(--sky-bottom) 78%);
    overflow: hidden;
  }
  .model-photo {
    position: absolute;
    left: 22px;
    top: 100px;
    width: 330px;
    height: 900px;
    background: linear-gradient(180deg, var(--photo-top) 0%, #9a8070 8%, var(--photo-suit) 16%, var(--photo-suit) 42%, var(--photo-trouser) 50%, var(--photo-trouser) 66%, var(--photo-stool) 74%, var(--photo-stool) 92%, var(--sky-bottom) 100%);
    border-radius: 24px;
  }
  .headline {
    position: absolute;
    left: 331px;
    top: 62px;
    width: 315px;
    text-align: center;
    font-family: "Arvo", serif;
    font-weight: 700;
    font-size: 40px;
    line-height: 1;
    letter-spacing: 1px;
    color: var(--navy);
  }
  .sale-badge {
    position: absolute;
    left: 331px;
    top: 120px;
    width: 315px;
    height: 425px;
  }
  .sale-badge svg { position: absolute; inset: 0; }
  .sale-word,
  .discount,
  .discount-off {
    position: absolute;
    width: 100%;
    text-align: center;
    line-height: 1;
    color: var(--navy);
  }
  .sale-word {
    top: 18px;
    font-family: "Arvo", serif;
    font-weight: 700;
    font-size: 88px;
    letter-spacing: 3px;
  }
  .discount {
    top: 146px;
    font-family: "Josefin Sans", sans-serif;
    font-weight: 300;
    font-size: 72px;
  }
  .discount-off {
    top: 228px;
    font-family: "Josefin Sans", sans-serif;
    font-weight: 300;
    font-size: 72px;
    letter-spacing: 4px;
  }
  .store-name {
    position: absolute;
    left: 366px;
    top: 808px;
    width: 300px;
    text-align: center;
    font-family: "Questrial", sans-serif;
    font-size: 88px;
    line-height: 1;
    color: var(--ink);
  }
  .store-type {
    position: absolute;
    left: 366px;
    top: 908px;
    width: 300px;
    text-align: center;
    font-family: "Questrial", sans-serif;
    font-size: 44px;
    line-height: 1;
    letter-spacing: 1px;
    color: var(--ink);
  }
</style>
</head>
<body>
  <div class="frame" aria-hidden="true"></div>
  <main class="poster">
    <div class="model-photo" role="img" aria-label="Photo of a man in a slim-fit navy suit and white trousers seated on a tall wooden bar stool"></div>

    <h1 class="headline">MEN'S SUIT</h1>

    <div class="sale-badge">
      <svg viewBox="0 0 315 425" width="315" height="425" aria-hidden="true">
        <polygon points="4,4 311,4 311,284 157.5,420 4,284" fill="none" stroke="var(--navy)" stroke-width="4"/>
        <polygon points="14,14 301,14 301,278 157.5,404 14,278" fill="none" stroke="var(--navy)" stroke-width="1.5"/>
        <line x1="30" y1="128" x2="285" y2="128" stroke="var(--navy)" stroke-width="4"/>
        <polygon points="157.5,332 161.5,342 172,342 163.5,348.5 166.5,359 157.5,352.5 148.5,359 151.5,348.5 143,342 153.5,342" fill="var(--navy)"/>
      </svg>
      <div class="sale-word">SALE</div>
      <div class="discount">40-60%</div>
      <div class="discount-off">OFF</div>
    </div>

    <div class="store-name">marlow</div>
    <div class="store-type">menswear</div>
  </main>
</body>
</html>
```